Brackwell HVAC Service LLC Business Card

We just got a design created by one of your designers for a logo and now would like help with a business card design. The information to be included on the card is as follows:
Brackwell HVAC Service LLC (I will attach logo design)
P.O. Box 418
Fairmont, CO 80639
(970) 374-6192
Milo Dunkirk
I might include an e-mail address, but I'm not sure yet.
Target Market(s)
Customers needing service or repairs done on their heating and air conditioning systems.
Industry/Entity Type
Business
Contact Information for Business Card
P.O. Box 418
Fairmont, CO 80639
(970) 374-6192
Milo Dunkirk

```html
<!DOCTYPE html>
<html lang="en">
<head>
<meta charset="utf-8">
<title>Brackwell HVAC Service LLC – Business Card</title>
<link href="https://fonts.googleapis.com/css2?family=Lato:wght@400;700;900&display=swap" rel="stylesheet">
<style>
  :root {
    --backdrop: #2b2b2b;
    --card: #efefef;
    --navy: #1b2a57;
    --red: #a11d22;
    --ink: #151515;
  }
  * { box-sizing: border-box; margin: 0; padding: 0; }
  html, body {
    width: 1200px; height: 1000px; overflow: hidden;
    background: var(--backdrop);
    font-family: "Lato", Arial, sans-serif;
  }
  .business-card {
    position: absolute; left: 150px; top: 243px;
    width: 900px; height: 514px;
    background: var(--card);
    overflow: hidden;
  }
  .brand {
    position: absolute; left: 64px; top: 86px;
    display: flex; align-items: center; gap: 26px;
  }
  .brand-dot {
    width: 112px; height: 112px; border-radius: 50%;
    background: var(--navy);
  }
  .brand-name {
    font-weight: 900; color: var(--navy);
    font-size: 44px; line-height: 1.05; letter-spacing: 1px;
    text-transform: uppercase;
  }
  .person-name {
    position: absolute; left: 64px; top: 292px;
    font-weight: 700; font-size: 29px; color: var(--ink);
    letter-spacing: 0.5px; text-transform: uppercase;
  }
  .contact-list {
    position: absolute; left: 70px; top: 342px;
    list-style: none;
  }
  .contact-item {
    display: flex; align-items: center; gap: 12px;
    font-size: 22px; color: var(--ink); line-height: 34px;
  }
  .contact-icon { width: 18px; height: 18px; flex: none; fill: var(--red); }
  .band { position: absolute; bottom: 0; height: 58px; }
  .band-navy { left: 0; width: 604px; background: var(--navy); }
  .band-red { left: 612px; right: 0; background: var(--red); }
</style>
</head>
<body>
  <div class="business-card">
    <div class="brand">
      <div class="brand-dot"></div>
      <div class="brand-name">Brackwell HVAC<br>Service LLC</div>
    </div>

    <div class="person-name">Milo Dunkirk</div>

    <ul class="contact-list">
      <li class="contact-item">
        <svg class="contact-icon" viewBox="0 0 24 24" aria-hidden="true"><path d="M6.6 10.8c1.4 2.8 3.8 5.1 6.6 6.6l2.2-2.2c.3-.3.7-.4 1-.2 1.1.4 2.3.6 3.6.6.6 0 1 .4 1 1V20c0 .6-.4 1-1 1C10.6 21 3 13.4 3 4c0-.6.4-1 1-1h3.5c.6 0 1 .4 1 1 0 1.3.2 2.5.6 3.6.1.3 0 .7-.2 1l-2.3 2.2z"/></svg>
        (970) 374-6192
      </li>
      <li class="contact-item">
        <svg class="contact-icon" viewBox="0 0 24 24" aria-hidden="true"><path d="M2 5h20v14H2z"/><path d="M2 6.5l10 7.5 10-7.5V5H2z" fill="#efefef"/></svg>
        milo@brackwellhvacservice.com
      </li>
      <li class="contact-item">
        <svg class="contact-icon" viewBox="0 0 24 24" aria-hidden="true"><path d="M12 2a7 7 0 0 0-7 7c0 5.2 7 13 7 13s7-7.8 7-13a7 7 0 0 0-7-7zm0 9.5A2.5 2.5 0 1 1 12 6.5a2.5 2.5 0 0 1 0 5z"/></svg>
        P.O. Box 418 Fairmont, CO 80639
      </li>
    </ul>

    <div class="band band-navy"></div>
    <div class="band band-red"></div>
  </div>
</body>
</html>
```